Webdesign für Lösungsanbieter für die Digitalisierung von Unternehmen
Zielgruppe
Wir sehen uns als Ihr Lösungsanbieter für die Digitalisierung Ihres Unternehmens. Durch unser breit aufgestelltes Leistungsportfolio sind wird in der Lage Sie mit Komplettlösungen im Bereich Bürokommunikation und Infrastruktur zu unterstützen.
Wir wünschen uns ein neues frisches Design, gerne etwas unkonventionell. Unsere Zielgruppe sind kleine bis Mittelständige Unternehmen. Labore sind die Zielgruppe für unsere eigenen Produkte. Des weiteren betreuen wir deutschlandweit Kunden im Cloudbereich und IP Telefonie.
Unsere Tätigkeit
- IT Systemhaus (Verkauf und Installation von IT Systemem)
- Softwareentwicklung (eingene Produkte sowie Auftragsentwicklungen für Kunden)
- IP Telefonsysteme
- Sicherheitstechnik
- Clouddiesnste (Rechnenzentrum, SaaS,IAAS)
- Webhosting
- Consulting
- Netzwerktechnik (Glasfaser und Kupfer).
Aufgabenstellung
Wir bitten um offene Daten.

```html
<!DOCTYPE html>
<html lang="de">
<head>
<meta charset="utf-8">
<title>Velantis – Integrierte Lösung für das digitale Zeitalter</title>
<link rel="stylesheet" href="https://fonts.googleapis.com/css2?family=Oswald:wght@400;500;700&family=Roboto:wght@400;500;700&display=swap">
<style>
:root{
  --navy:#15152d;
  --navy-2:#1d1f3d;
  --orange:#e8821e;
  --green:#b8be3f;
  --gold:#cdb64d;
  --light:#f2f2f2;
  --card:#efefef;
  --text:#222;
  --muted:#555;
  --white:#fff;
}
*{box-sizing:border-box;margin:0;padding:0}
html,body{width:1200px;height:3721px;overflow:hidden}
body{position:relative;font-family:'Roboto',sans-serif;color:var(--text);background:var(--white)}
.abs{position:absolute}
.photo{position:absolute;display:block}

/* Hero */
.hero{position:absolute;left:0;top:0;width:1200px;height:440px;background:var(--navy);overflow:hidden}
.hero-visual{left:500px;top:0;width:700px;height:390px;background:radial-gradient(ellipse at 45% 40%,#3a7fc0 0%,#1e3f78 35%,#141a36 70%),var(--navy);opacity:.95}
.brand{position:absolute;display:flex;align-items:center;gap:10px;font-family:'Roboto',sans-serif;font-weight:400;color:var(--white)}
.brand-dot{width:26px;height:26px;border-radius:50%;background:var(--orange)}
.brand-name{font-size:34px;letter-spacing:1px}
.nav{position:absolute;top:56px;left:535px;display:flex;gap:23px;align-items:center;font-size:11px;font-weight:500;color:var(--white);text-transform:uppercase}
.nav .active{color:var(--orange)}
.nav .btn-contact{background:var(--orange);padding:9px 16px;margin-left:10px;color:var(--white)}
.hero-kicker{left:174px;top:139px;font-size:10px;font-weight:500;color:var(--gold);text-transform:uppercase}
.hero-title{left:172px;top:156px;font-family:'Oswald',sans-serif;font-weight:700;font-size:46px;line-height:52px;color:var(--white);text-transform:uppercase}
.hero-text{left:174px;top:322px;width:290px;font-size:12px;line-height:17px;color:#d6d7e2}
.hero-swoosh{left:0;top:340px;width:1200px;height:100px}

/* Section headings */
.sec-mark{width:30px;height:30px;border-radius:50%;background:var(--orange);left:585px}
.sec-kicker{left:0;width:1200px;text-align:center;font-size:12px;color:var(--orange);text-transform:uppercase}
.sec-title{left:0;width:1200px;text-align:center;font-size:19px;font-weight:700;color:var(--navy);text-transform:uppercase;letter-spacing:.3px}

/* Service cards */
.service{position:absolute;width:208px;height:267px;border:1px solid #e2e2e2;background:var(--white);text-align:center}
.service .photo{position:relative;width:100%;height:115px}
.service h3{font-size:11px;font-weight:500;margin-top:21px;text-transform:uppercase;color:var(--text)}
.service p{font-size:9px;line-height:12px;color:var(--muted);margin:12px 20px 0}
.btn-outline{display:inline-block;margin-top:17px;border:1px solid var(--orange);color:var(--orange);font-size:8.5px;padding:7px 14px}

/* CTA band */
.cta{left:0;top:1271px;width:1200px;height:159px;background:linear-gradient(90deg,#16163a,#222650 50%,#16163a);border-top:6px solid var(--orange)}
.cta-line{position:absolute;left:900px;top:-6px;width:300px;height:6px;background:var(--green)}
.cta h2{position:absolute;left:0;top:26px;width:1200px;text-align:center;font-family:'Roboto',sans-serif;font-weight:500;font-size:29px;color:var(--white);text-transform:uppercase}
.cta p{position:absolute;left:0;top:66px;width:1200px;text-align:center;font-size:11px;color:#d0d1dc}
.cta-phone{position:absolute;left:415px;top:92px;font-family:'Oswald',sans-serif;font-weight:400;font-size:22px;color:var(--gold)}
.cta-sep{position:absolute;left:593px;top:96px;width:2px;height:26px;background:var(--white)}
.cta-btn{position:absolute;left:611px;top:94px;background:var(--orange);color:var(--white);font-size:9px;font-weight:500;padding:10px 18px;border-radius:16px;text-transform:uppercase}

/* About */
.about{left:0;top:1430px;width:1200px;height:325px;background:var(--light);overflow:hidden}
.about-kicker{left:174px;top:106px;font-size:12px;color:var(--orange);text-transform:uppercase}
.about-title{left:174px;top:127px;font-size:18.5px;line-height:25px;font-weight:700;color:#333;text-transform:uppercase}
.about-rule{left:469px;top:100px;width:1px;height:96px;background:#cfcfcf}
.about-sub{left:502px;top:95px;font-size:12px;font-weight:500;color:var(--text)}
.about-text{left:502px;top:123px;width:510px;font-size:9.5px;line-height:14px;color:var(--muted)}
.pill{position:absolute;background:var(--orange);color:var(--white);font-size:10px;border-radius:14px;padding:7px 18px}

/* Why us */
.why{left:0;top:1755px;width:1200px;height:570px;background:var(--navy);overflow:hidden}
.why-kicker{left:630px;top:70px;font-size:12px;color:var(--gold);text-transform:uppercase}
.why-title{left:630px;top:93px;font-size:24px;line-height:35px;font-weight:700;color:var(--white);text-transform:uppercase}
.why-text{left:631px;top:176px;width:330px;font-size:10px;line-height:14px;color:#c9cad6}
.feature{position:absolute;left:628px;width:340px;display:flex;gap:14px}
.feature svg{flex:none;width:26px;height:26px}
.feature h4{font-size:12px;font-weight:500;color:var(--orange)}
.feature p{font-size:9px;line-height:13px;font-weight:700;color:#e6e6ee;margin-top:5px;width:230px}

/* News */
.news{position:absolute;width:223px;height:355px;background:var(--card);border-radius:6px;overflow:hidden}
.news .photo{position:relative;width:100%;height:140px}
.news-date{position:absolute;right:14px;top:116px;width:42px;height:35px;background:var(--orange);color:var(--white);font-size:9px;line-height:11px;text-align:center;padding-top:6px;border-radius:3px 3px 0 0}
.news-cat{margin:20px 0 0 19px;font-size:8.5px;color:var(--orange);display:flex;align-items:center;gap:6px}
.news h3{margin:14px 19px 0;font-size:13px;line-height:16px;font-weight:500;color:var(--text)}
.news p{margin:14px 19px 0;font-size:8.5px;line-height:13px;color:var(--muted)}
.news .arrow{position:absolute;left:21px;bottom:40px;width:43px;height:24px;border-radius:12px;background:var(--orange);color:var(--white);font-size:12px;text-align:center;line-height:24px}

/* Contact */
.contact{left:0;top:2940px;width:1200px;height:480px;background:#f1f1f1}
.contact-shadow{left:272px;top:82px;width:222px;height:337px;background:var(--green)}
.contact-box{left:258px;top:66px;width:223px;height:337px;background:var(--orange);color:var(--white)}
.contact-item{position:absolute;left:16px;display:flex;gap:12px;width:190px}
.contact-item svg{flex:none;width:24px;height:24px;margin-top:6px}
.contact-item h4{font-size:17px;font-weight:500}
.contact-item p{font-size:9px;line-height:11px;margin-top:1px}
.contact-rule{position:absolute;left:16px;width:190px;height:1px;background:rgba(255,255,255,.45)}
.form-kicker{left:537px;top:87px;font-size:11px;color:var(--orange);text-transform:uppercase}
.form-title{left:537px;top:107px;font-size:15px;font-weight:700;color:#222;text-transform:uppercase}
.field{position:absolute;border-bottom:1px solid #b9b9b9;font-size:9.5px;color:var(--orange);padding-bottom:10px}

/* Footer */
.footer{left:0;top:3408px;width:1200px;height:313px;background:var(--navy)}
.footer-swoosh{left:0;top:3370px;width:1200px;height:120px}
.footer-nav{left:0;top:3533px;width:1200px;display:flex;justify-content:center;gap:26px;font-size:11px;color:var(--white);text-transform:uppercase}
.copyright{left:0;top:3562px;width:1200px;text-align:center;font-size:10px;color:var(--white)}
</style>
</head>
<body>

<!-- Hero -->
<section class="hero">
  <div class="photo hero-visual" role="img" aria-label="Glühendes Datennetz über einer nächtlichen Weltkarte"></div>
  <div class="brand" style="left:174px;top:38px"><span class="brand-dot"></span><span class="brand-name">velantis</span></div>
  <nav class="nav">
    <span class="active">Startseite</span><span>Dienstleistungen</span><span>Preis</span><span>Über uns</span><span>Blog</span><span class="btn-contact">Kontakt</span>
  </nav>
  <div class="abs hero-kicker">Wir sind ein führendes Technologieunternehmen</div>
  <h1 class="abs hero-title">Integrierte Lösung<br>für das digitale<br>Zeitalter</h1>
  <p class="abs hero-text">Orem ipsum dolor sit amet, consectetur adipiscing elit utelit tellus, luctus nec ullam corper mattis, pulvinar dapibus leo nulla metus.</p>
</section>
<svg class="abs hero-swoosh" viewBox="0 0 1200 100" preserveAspectRatio="none">
  <path d="M0 45 C250 75 500 80 760 45 C950 20 1100 10 1200 25 L1200 100 L0 100Z" fill="var(--orange)"/>
  <path d="M0 50 C120 70 180 85 300 90 C200 92 90 85 0 78Z" fill="var(--green)"/>
  <path d="M0 70 C300 100 600 95 850 70 C1000 55 1120 48 1200 50 L1200 100 L0 100Z" fill="#fff"/>
</svg>

<!-- Services -->
<div class="abs sec-mark" style="top:498px"></div>
<div class="abs sec-kicker" style="top:552px">Wir bieten ein breites</div>
<h2 class="abs sec-title" style="top:574px">Vielzahl von Digitalisierungslösungen</h2>

<article class="service" style="left:173px;top:650px"><div class="photo" role="img" aria-label="Hand mit Werkzeug an Netzwerkkabeln" style="background:linear-gradient(135deg,#ddd,#e58a3a 55%,#333)"></div><h3>IT Systemhaus</h3><p>Lorem ipsum dolor sit amet, consectetur adipiscing elit. Ut elit tellus, luctus nec ulla-mcorper mattis, pulvinar dapibus leo.</p><span class="btn-outline">Weiterlesen</span></article>
<article class="service" style="left:388px;top:650px"><div class="photo" role="img" aria-label="Hände tippen vor leuchtenden Code-Symbolen" style="background:linear-gradient(135deg,#5a3a2a,#e89a56 50%,#3b2a22)"></div><h3>Softwareentwicklung</h3><p>Lorem ipsum dolor sit amet, consectetur adipiscing elit. Ut elit tellus, luctus nec ulla-mcorper mattis, pulvinar dapibus leo.</p><span class="btn-outline">Weiterlesen</span></article>
<article class="service" style="left:604px;top:650px"><div class="photo" role="img" aria-label="IP-Telefon vor einem Serverschrank" style="background:linear-gradient(135deg,#2a3550,#6b7b9b 50%,#1b2236)"></div><h3>IP Telefonsysteme</h3><p>Lorem ipsum dolor sit amet, consectetur adipiscing elit. Ut elit tellus, luctus nec ulla-mcorper mattis, pulvinar dapibus leo.</p><span class="btn-outline">Weiterlesen</span></article>
<article class="service" style="left:817px;top:650px"><div class="photo" role="img" aria-label="Digitales Schutzschild über einer Stadt" style="background:radial-gradient(circle at 50% 45%,#7fb4f0,#1f56b8 50%,#0c2a6a)"></div><h3>Sicherheitstechnik</h3><p>Lorem ipsum dolor sit amet, consectetur adipiscing elit. Ut elit tellus, luctus nec ulla-mcorper mattis, pulvinar dapibus leo.</p><span class="btn-outline">Weiterlesen</span></article>

<article class="service" style="left:173px;top:931px"><div class="photo" role="img" aria-label="Laptop mit Cloud-Symbolen auf einem Schreibtisch" style="background:linear-gradient(135deg,#c9a063,#4a3a28 55%,#1d1812)"></div><h3>Clouddiesnste</h3><p>Lorem ipsum dolor sit amet, consectetur adipiscing elit. Ut elit tellus, luctus nec ulla-mcorper mattis, pulvinar dapibus leo.</p><span class="btn-outline">Weiterlesen</span></article>
<article class="service" style="left:388px;top:931px"><div class="photo" role="img" aria-label="Gang zwischen Serverreihen im Rechenzentrum" style="background:linear-gradient(90deg,#222,#9a9a9a 50%,#222)"></div><h3>Webhosting</h3><p>Lorem ipsum dolor sit amet, consectetur adipiscing elit. Ut elit tellus, luctus nec ulla-mcorper mattis, pulvinar dapibus leo.</p><span class="btn-outline">Weiterlesen</span></article>
<article class="service" style="left:604px;top:931px"><div class="photo" role="img" aria-label="Beratungsgespräch mit Unterlagen am Tisch" style="background:linear-gradient(135deg,#4a6a8a,#e6eaf0 50%,#8fa2b8)"></div><h3>Consulting</h3><p>Lorem ipsum dolor sit amet, consectetur adipiscing elit. Ut elit tellus, luctus nec ulla-mcorper mattis, pulvinar dapibus leo.</p><span class="btn-outline">Weiterlesen</span></article>
<article class="service" style="left:817px;top:931px"><div class="photo" role="img" aria-label="Leuchtendes Glasfaserkabel" style="background:radial-gradient(ellipse at 55% 50%,#ffd08a,#e8501e 35%,#1a2a4a 75%)"></div><h3>Netzwerktechnik</h3><p>Lorem ipsum dolor sit amet, consectetur adipiscing elit. Ut elit tellus, luctus nec ulla-mcorper mattis, pulvinar dapibus leo.</p><span class="btn-outline">Weiterlesen</span></article>

<!-- CTA -->
<section class="abs cta">
  <span class="cta-line"></span>
  <h2>Kostenlose Erstberatung</h2>
  <p>Jetzt Termin vereinbaren und 30 Minuten kostenlose Beratung erhalten.</p>
  <span class="cta-phone">+49 30 55 | 218 40-0</span>
  <span class="cta-sep"></span>
  <span class="cta-btn">Planen Sie Ihr Meeting</span>
</section>

<!-- About -->
<section class="abs about">
  <div class="abs about-kicker">Über unsere Firma</div>
  <h2 class="abs about-title">Wir helfen Unternehmen,<br>im digitalen Zeitalter<br>voranzukommen</h2>
  <span class="abs about-rule"></span>
  <h3 class="abs about-sub">Dies ist die Hauptüberschrift</h3>
  <p class="abs about-text">Lorem ipsum dolor sit amet, consectetur adipiscing elit, sed do eiusmod tempor incididunt ut labore et dolore magna aliqua. Ut enim ad minim veniam, quis nostrud exercitation ullamco laboris nisi ut aliquip ex ea commodo consequat.</p>
  <span class="pill" style="left:501px;top:169px">View All →</span>
</section>

<!-- Why us -->
<section class="abs why">
  <svg class="abs" style="left:0;top:0" width="620" height="570" viewBox="0 0 620 570">
    <defs><linearGradient id="teamTone" x1="0" y1="0" x2="1" y2="1"><stop offset="0" stop-color="#8a8f9a"/><stop offset=".5" stop-color="#5a4a48"/><stop offset="1" stop-color="#2e3140"/></linearGradient></defs>
    <path d="M0 0 L460 0 C560 80 610 220 560 330 C520 420 380 470 0 545Z" fill="var(--green)"/>
    <path d="M0 0 L430 0 C530 90 580 230 530 330 C490 410 360 450 0 530Z" fill="url(#teamTone)" role="img" aria-label="Team im Besprechungsraum"/>
    <path d="M0 530 C300 470 500 420 600 330 C560 450 380 520 0 570Z" fill="var(--orange)"/>
  </svg>
  <div class="abs why-kicker">Warum uns wählen</div>
  <h2 class="abs why-title">Seit über 30 Jahren in<br>der Technologiebranche</h2>
  <p class="abs why-text">Lorem ipsum dolor sit amet, consectetur adipiscing elit, sed do eiusmod tempor incididunt ut labore et dolore magna aliqua. Ut enim ad minim veniam, quis nostrud exercitation ullamco laboris nisi ut aliquip ex ea com-modo consequat.</p>
  <div class="feature" style="top:272px"><svg viewBox="0 0 26 26" fill="none" stroke="var(--orange)" stroke-width="1.6"><circle cx="13" cy="13" r="11"/><circle cx="13" cy="13" r="5"/><path d="M5 5l4 4M21 5l-4 4M5 21l4-4M21 21l-4-4"/></svg><div><h4>Experten für technischen Support</h4><p>Diam vel quam elementum pulvinar ac tium aenean pharetra magna ac placerat quis eget.</p></div></div>
  <div class="feature" style="top:341px"><svg viewBox="0 0 26 26" fill="none" stroke="var(--orange)" stroke-width="1.6"><path d="M13 2l3.3 7 7.7.9-5.7 5.2 1.6 7.6L13 18.9 6.1 22.7l1.6-7.6L2 9.9 9.7 9Z"/></svg><div><h4>Solide Teamarbeit</h4><p>Diam vel quam elementum pulvinar ac tium aenean pharetra magna ac placerat quis eget.</p></div></div>
  <div class="feature" style="top:410px"><svg viewBox="0 0 26 26" fill="none" stroke="var(--orange)" stroke-width="1.6"><rect x="2" y="3" width="22" height="6"/><rect x="2" y="10" width="22" height="6"/><rect x="2" y="17" width="22" height="6"/><path d="M5 6h2M5 13h2M5 20h2"/></svg><div><h4>Fortschrittliche Technologie</h4><p>Diam vel quam elementum pulvinar ac tium aenean pharetra magna ac placerat quis eget.</p></div></div>
</section>

<!-- News -->
<div class="abs sec-mark" style="top:2360px"></div>
<div class="abs sec-kicker" style="top:2410px">Bleiben Sie mit Velantis auf dem Laufenden</div>
<h2 class="abs sec-title" style="top:2432px">Von den neuesten &amp; beliebten News</h2>

<article class="news" style="left:243px;top:2503px"><div class="photo" role="img" aria-label="Nahaufnahme einer Maschinenspindel" style="background:linear-gradient(135deg,#bfc2c8,#4a4f5a 50%,#1c2028)"></div><span class="news-date">July 19<br>2021</span><div class="news-cat"><svg width="10" height="8" viewBox="0 0 10 8" fill="none" stroke="var(--orange)"><path d="M.5 .5h3l1 1h5v6h-9z"/></svg>Artificial Store</div><h3>Repeated of endeavor mr position kindness.</h3><p>Lorem ipsum dolor sit amet, consectetur adipiscing elit, sed do eiusmod tempor incid-idunt ut labore.</p><span class="arrow">→</span></article>
<article class="news" style="left:488px;top:2503px"><div class="photo" role="img" aria-label="Zwei Techniker an einer Roboterwerkbank" style="background:linear-gradient(135deg,#7fa6c8,#3c5a78 50%,#c49a70)"></div><span class="news-date">July 19<br>2021</span><div class="news-cat"><svg width="10" height="8" viewBox="0 0 10 8" fill="none" stroke="var(--orange)"><path d="M.5 .5h3l1 1h5v6h-9z"/></svg>Automation</div><h3>Justifying Automation in Your Factory.</h3><p>Lorem ipsum dolor sit amet, consectetur adipiscing elit, sed do eiusmod tempor incid-idunt ut labore.</p><span class="arrow">→</span></article>
<article class="news" style="left:732px;top:2503px"><div class="photo" role="img" aria-label="Industrieroboterarm in einer Fertigungshalle" style="background:linear-gradient(135deg,#9aa0a8,#d6d8dc 50%,#555b64)"></div><span class="news-date">July 19<br>2021</span><div class="news-cat"><svg width="10" height="8" viewBox="0 0 10 8" fill="none" stroke="var(--orange)"><path d="M.5 .5h3l1 1h5v6h-9z"/></svg>Digitalization</div><h3>Boost Your Cobot Safety Know-How with These Digital Resources</h3><p>Lorem ipsum dolor sit amet, consectetur adipiscing elit, sed do eiusmod tempor incid-idunt ut labore.</p><span class="arrow">→</span></article>

<!-- Contact -->
<section class="abs contact">
  <div class="abs contact-shadow"></div>
  <div class="abs contact-box">
    <div class="contact-item" style="top:68px"><svg viewBox="0 0 24 24" fill="#fff"><path d="M12 2a6 6 0 0 0-6 6c0 4.5 6 12 6 12s6-7.5 6-12a6 6 0 0 0-6-6zm0 8.3a2.3 2.3 0 1 1 0-4.6 2.3 2.3 0 0 1 0 4.6z"/></svg><div><h4>Velantis GmbH</h4><p>Lindenallee 12<br>40210 Musterstadt</p></div></div>
    <span class="contact-rule" style="top:130px"></span>
    <div class="contact-item" style="top:154px"><svg viewBox="0 0 24 24" fill="#fff"><path d="M6.6 10.8a15.1 15.1 0 0 0 6.6 6.6l2.2-2.2a1 1 0 0 1 1-.25 11.4 11.4 0 0 0 3.6.57 1 1 0 0 1 1 1V20a1 1 0 0 1-1 1A17 17 0 0 1 3 4a1 1 0 0 1 1-1h3.5a1 1 0 0 1 1 1c0 1.25.2 2.45.57 3.6a1 1 0 0 1-.25 1z"/></svg><div><h4>Einen Anruf tätigen</h4><p>+49 30 55 | 218 40-0</p></div></div>
    <span class="contact-rule" style="top:211px"></span>
    <div class="contact-item" style="top:240px"><svg viewBox="0 0 24 24" fill="#fff"><path d="M2 9l10-6 10 6v11H2zm2 1.2V18h16v-7.8l-8 5z"/></svg><div><h4>Senden Sie eine E-Mail</h4><p>vertrieb@velantis.de</p></div></div>
  </div>
  <div class="abs form-kicker">Wir freuen uns jederzeit von Ihnen zu hören</div>
  <h2 class="abs form-title">Machen Sie sich bereit, Ihr Projekt mit uns zu starten</h2>
  <div class="field" style="left:537px;top:164px;width:412px">Name</div>
  <div class="field" style="left:537px;top:207px;width:188px">Email*</div>
  <div class="field" style="left:762px;top:207px;width:187px">Phone</div>
  <div class="field" style="left:537px;top:250px;width:412px;height:92px">Tell Us About Project*</div>
  <span class="pill" style="left:537px;top:385px;padding:6px 16px">Send Message ➤</span>
</section>

<!-- Footer -->
<section class="abs footer"></section>
<svg class="abs footer-swoosh" viewBox="0 0 1200 120" preserveAspectRatio="none">
  <rect x="0" y="0" width="1200" height="120" fill="var(--navy)"/>
  <path d="M0 0 H1200 V30 C1000 20 800 40 600 70 C400 95 200 90 0 70Z" fill="var(--orange)"/>
  <path d="M0 0 H1200 V22 C1000 12 800 32 600 60 C400 88 220 84 0 55Z" fill="var(--green)"/>
  <path d="M0 0 H1200 V14 C1000 6 800 26 600 50 C400 74 200 72 0 45Z" fill="#f1f1f1"/>
</svg>
<nav class="abs footer-nav"><span>Startseite</span><span>Dienstleistungen</span><span>Preis</span><span>Über uns</span><span>Blog</span><span>Kontakt</span></nav>
<div class="abs copyright">COPYRIGHT © 2021. ALL RIGHTS RESERVED.</div>
<div class="brand" style="left:470px;top:3620px"><span class="brand-dot" style="width:34px;height:34px"></span><span class="brand-name" style="font-size:46px">velantis</span></div>

</body>
</html>
```